Afternoon Soiree Garden Party Invitation

Invitation design for an 'Afternoon Soirée' backyard garden party.
Format is for-print and mailing and can be either double-sided design to be enveloped and mailed or it can be a postcard-style with design on one side and address/postage placeholder on the reverse side.
Text, dimensions and additional information in the provided Word document.
Font styles to use
Script
Requirements
Must have
- Elegant, yet easy-going and warm/welcoming feel

```html
<!DOCTYPE html>
<html lang="en">
<head>
<meta charset="utf-8">
<title>Afternoon Soirée Invitation</title>
<link rel="stylesheet" href="https://fonts.googleapis.com/css2?family=Montserrat:wght@700;800;900&family=Great+Vibes&family=Raleway:wght@300;600&display=swap">
<style>
  :root {
    --ink: #ffffff;
    --ink-soft: rgba(255,255,255,0.85);
    --forest: #1f3a2a;
    --night: #1c2f45;
    --dusk: #2a3a4e;
    --ember: #c9743a;
    --earth: #5a3328;
    --moss: #2f4a2a;
  }
  * { margin: 0; padding: 0; box-sizing: border-box; }
  html, body { width: 779px; height: 1200px; overflow: hidden; background: #1a2630; }
  .invitation {
    position: relative;
    width: 779px;
    height: 1200px;
    overflow: hidden;
    color: var(--ink);
  }
  .garden-scene {
    position: absolute; inset: 0;
    background:
      radial-gradient(ellipse 160px 150px at 395px 860px, rgba(255,205,120,0.85), rgba(201,116,58,0.5) 45%, transparent 75%),
      radial-gradient(ellipse 420px 360px at 420px 860px, rgba(120,60,40,0.85), transparent 75%),
      radial-gradient(ellipse 300px 260px at 80px 300px, rgba(47,90,42,0.85), transparent 70%),
      radial-gradient(ellipse 360px 300px at 620px 200px, rgba(45,75,110,0.9), transparent 70%),
      linear-gradient(180deg, var(--forest) 0%, var(--night) 30%, var(--dusk) 48%, var(--earth) 72%, #3a2a2a 88%, var(--moss) 100%);
  }
  .afternoon {
    position: absolute; left: 0; top: 0; width: 779px; height: 200px;
  }
  .afternoon text {
    font-family: "Montserrat", sans-serif;
    font-weight: 800;
    font-size: 36px;
    fill: var(--ink);
  }
  .soiree {
    position: absolute; left: 0; width: 779px; top: 195px;
    text-align: center;
    font-family: "Great Vibes", cursive;
    font-weight: 400;
    font-size: 160px;
    line-height: 1;
  }
  .venue {
    position: absolute; left: 0; width: 779px; top: 379px;
    text-align: center;
    font-family: "Montserrat", sans-serif;
    font-weight: 800;
    font-size: 25px;
    letter-spacing: 2.5px;
    line-height: 38px;
  }
  .date {
    position: absolute; left: 0; width: 779px; top: 498px;
    display: flex; justify-content: center; align-items: center;
    height: 80px;
  }
  .date .day {
    font-family: "Great Vibes", cursive;
    font-size: 72px;
    margin-right: 12px;
  }
  .date .num {
    font-family: "Montserrat", sans-serif;
    font-weight: 900;
    font-size: 70px;
    letter-spacing: 4px;
    padding: 0 10px;
  }
  .date .rule {
    width: 4px; height: 62px; background: var(--ink);
  }
  .time {
    position: absolute; left: 0; width: 779px; top: 622px;
    text-align: center;
    font-family: "Great Vibes", cursive;
    font-size: 52px;
    line-height: 1;
  }
  .weather {
    position: absolute; left: 0; width: 779px; top: 678px;
    text-align: center;
    font-family: "Raleway", sans-serif;
    font-weight: 300;
    font-size: 14px;
    letter-spacing: 3.5px;
    color: var(--ink-soft);
  }
  .notes {
    position: absolute; left: 0; width: 779px; top: 1125px;
    text-align: center;
    font-family: "Raleway", sans-serif;
    font-weight: 600;
    font-size: 17px;
    line-height: 20px;
  }
</style>
</head>
<body>
<main class="invitation">
  <div class="garden-scene" role="img" aria-label="Painted evening backyard scene: guests gathered under trees with string lights around a glowing fire pit with striped blankets"></div>

  <svg class="afternoon" viewBox="0 0 779 200" aria-label="Afternoon">
    <defs>
      <path id="arc" d="M 228 166 Q 390 96 552 166"/>
    </defs>
    <text><textPath href="#arc" startOffset="50%" text-anchor="middle" textLength="330" lengthAdjust="spacing">AFTERNOON</textPath></text>
  </svg>

  <h1 class="soiree">Soirée</h1>

  <p class="venue">MARLOW RESIDENCE<br>428 FENWICK AVE.</p>

  <div class="date">
    <span class="day">Fri</span>
    <span class="rule"></span>
    <span class="num">07</span>
    <span class="rule"></span>
    <span class="num">17</span>
    <span class="rule"></span>
    <span class="num">2020</span>
  </div>

  <p class="time">4:00 – 8:00 Pm</p>
  <p class="weather">WEATHER PERMITTING</p>

  <p class="notes">Please call 555-014-2287 if unsure.<br>This is a 19+ event.</p>
</main>
</body>
</html>
```